Design Card that Captures Life's Moments

Thinking black and white design with maybe some accent colors. Open to others too. Looking for bold and modern to accompany new logo design. For the side without my info, would have tagline of "Capturing Life's Moments" with either logo or website tessabrimphotography.com. I want the tagline to dominate and be the main focus of that side.

Target Market(s)

Something that can appeal to people who might be interested in family/kids, business, sports, commercial, or birth/newborn photography.

Industry/Entity Type

Professional Photography

Contact Information for Business Card

Font styles to use
Sans Serif
Script
Other font styles liked:
• Go with Logo, but the tagline could be script that popped.

Requirements
Must have
• See details above! Wow factor! Make someone pick my card up and take it home or at least to look at it further.
• Tagline: Capturing Life's Moments (Main text on side without name)
• INFO:
• Tessa Brimford-Kole - Photographer
• 555-213-0476 - Cell and for SMS
• www.tessabrimphotography.com - Website (maybe on side with tagline?)
• tessa@tessaphotographs.com - Email
Nice to have
• JUST AN IDEA... I would like to see Capturing Life's Moment really take over most of one side of the card. Think greeting card. Where you can't miss it. It is in your face, but nice and elegant. Maybe cursive, but could work with other font. Instead of logo on tagline side, just have tessabrimphotography.com in smaller text along one of the edges.
Should not have
• Too simple I could of created it, like with only my logo and some typed text.

```html
<!DOCTYPE html>
<html lang="en">
<head>
<meta charset="utf-8">
<title>Tessa Brim Photography — Business Card</title>
<link rel="stylesheet" href="https://fonts.googleapis.com/css2?family=Roboto+Condensed:ital,wght@1,300;1,400&family=Source+Sans+3:wght@300;400&display=swap">
<style>
  :root {
    --backdrop: #0a9bd6;
    --card-dark: #231f20;
    --card-light: #ffffff;
    --ink: #231f20;
    --ink-reversed: #ffffff;
    --shadow: rgba(0, 40, 70, 0.28);
  }
  * { box-sizing: border-box; margin: 0; padding: 0; }
  html, body {
    width: 1200px;
    height: 1200px;
    overflow: hidden;
    background: var(--backdrop);
  }
  .sheet {
    width: 1200px;
    height: 1200px;
    display: flex;
    flex-direction: column;
    align-items: center;
    justify-content: center;
    gap: 60px;
  }
  .card {
    width: 840px;
    height: 480px;
    position: relative;
    box-shadow: 0 10px 24px var(--shadow);
  }
  .card--front { background: var(--card-dark); }
  .card--back {
    background: var(--card-light);
    color: var(--ink);
    display: flex;
    flex-direction: column;
    align-items: center;
    justify-content: center;
    text-align: center;
  }

  /* Brand name, front side */
  .brand {
    position: absolute;
    right: 70px;
    bottom: 110px;
    color: var(--ink-reversed);
    font-family: "Source Sans 3", sans-serif;
    font-weight: 300;
    text-align: right;
  }
  .brand__name {
    display: block;
    font-size: 76px;
    line-height: 1;
  }
  .brand__trade {
    display: block;
    margin-top: 6px;
    font-size: 21px;
    letter-spacing: 0.42em;
    text-transform: uppercase;
    margin-right: -0.42em;
  }

  /* Back side */
  .tagline {
    font-family: "Roboto Condensed", sans-serif;
    font-style: italic;
    font-weight: 400;
    font-size: 44px;
    letter-spacing: 0.14em;
    margin-bottom: 44px;
  }
  .holder__name {
    font-family: "Source Sans 3", sans-serif;
    font-weight: 400;
    font-size: 31px;
    line-height: 1.15;
  }
  .holder__role {
    font-family: "Roboto Condensed", sans-serif;
    font-style: italic;
    font-weight: 300;
    font-size: 27px;
    margin-bottom: 26px;
  }
  .contact {
    list-style: none;
    font-family: "Source Sans 3", sans-serif;
    font-weight: 400;
    font-size: 26px;
    line-height: 1.38;
  }
</style>
</head>
<body>
  <main class="sheet">
    <section class="card card--front" aria-label="Card front">
      <p class="brand">
        <span class="brand__name">Tessa Brim</span>
        <span class="brand__trade">Photography</span>
      </p>
    </section>

    <section class="card card--back" aria-label="Card back">
      <h1 class="tagline">Capturing Life's Moments</h1>
      <p class="holder__name">Tessa Brimford-Kole</p>
      <p class="holder__role">Photographer</p>
      <ul class="contact">
        <li>Email: tessa@tessaphotographs.com</li>
        <li>Website: www.tessabrimphotography.com</li>
        <li>Call/SMS: 555-213-0476</li>
      </ul>
    </section>
  </main>
</body>
</html>
```